Photography business needs a money-off coupon design to be sent out by text

I'm a headshot photographer and I want to start a 'refer a friend' programme. Each time I take someone's headshot, I want to be able to give them a money-off coupon, featuring their own headshot, that they can send to their own network by text, offering a 20% discount to the recipient on a headshot session.

I need the design as a layered PSD file, so that I can drop in a different headshot for each client. Because the coupon will be being sent by text, I need it to be as simple and striking as possible. The design should meet the following criteria:

- It should feature my logo (two versions attached)

- It should feature one headshot - needs to be the main feature of the design. I have attached three examples from a typical session - as you will see, I use different backgrounds, so the design should be able to accommodate different colours.

- The following copy:

Milo Gives You 20% off (name will change with different headshots)

£30 off your next headshot session
Just text this referral card to make your appointment
Owen Hartley 07942 316 587
Normal Price £150, Now £130
www.framebrightly.co.uk

- The design should be portrait rather than landscape, given that that's how most people tend to use their phones vertically when they first look at a text message

- I need the designer to think about how the coupon will render on mobile phones; I think that it probably makes most sense to size the image in line with whichever smartphone has the highest resolution screen (probably vireo k4 or lumo 5), as that way the image will look good on all phone screens. Although I am happy to take the designer's advice on this and on optimum aspect ratio.

- Any other advice the designer can give me about the optimal design for text marketing of this nature will strongly impact on my final decision.

PLEASE NOTE: I've just uploaded a very basic layout that I did in Adobe Spark - I'm not expecting designers to follow it, but it does contain the key elements

Thanks,

Owen

Target Market(s)

Actors

Industry/Entity Type

Photographer

Font styles to use
Sans Serif

Colors

Designer to choose colors to be used in the design.

Requirements
Must have
• Clear communication of discount and redemption mechanism. Headshot image to be the most prominent feature. Must render clearly in different types of smartphone
Nice to have
• If possible, a link to my website (don't know if this is technically possible)
Should not have
• Colours which clash with my logo / the featured image

```html
<!DOCTYPE html>
<html lang="en">
<head>
<meta charset="utf-8">
<title>Frame Brightly – Referral Coupon</title>
<link rel="stylesheet" href="https://fonts.googleapis.com/css2?family=Hind:wght@400;500;600;700&display=swap">
<style>
  :root {
    --stage: #cdd3dc;
    --panel: #656668;
    --ink: #ffffff;
    --ink-soft: #e4e4e4;
    --mark: #9a9b9d;
    --outdoor-sky: #d9e4ea;
    --outdoor-mid: #9fb2a4;
    --outdoor-grass: #6f8f52;
    --studio-warm: #e1a94e;
    --studio-deep: #d49a3c;
  }
  * { box-sizing: border-box; margin: 0; padding: 0; }
  html, body { width: 1200px; height: 1000px; overflow: hidden; }
  body {
    background: var(--stage);
    font-family: "Hind", Arial, sans-serif;
    color: var(--ink);
    position: relative;
  }
  .coupon {
    position: absolute;
    top: 150px;
    width: 332px;
    height: 696px;
    background: var(--panel);
    border-radius: 30px;
    overflow: hidden;
  }
  .coupon--outdoor { left: 168px; }
  .coupon--studio { left: 712px; }

  .coupon__header { position: relative; height: 182px; }
  .brand {
    position: absolute;
    left: 30px;
    top: 64px;
    width: 80px;
    display: flex;
    align-items: flex-start;
    gap: 6px;
  }
  .brand__square {
    flex: none;
    width: 12px;
    height: 12px;
    margin-top: 4px;
    background: var(--mark);
  }
  .brand__name {
    font-size: 17px;
    line-height: 18px;
    font-weight: 500;
    color: var(--ink-soft);
  }
  .contact {
    position: absolute;
    left: 145px;
    top: 64px;
    font-size: 15.5px;
    line-height: 19px;
    font-weight: 400;
  }
  .contact__web {
    display: block;
    margin-top: 9px;
    font-size: 13px;
    font-weight: 500;
    color: var(--ink);
    text-decoration: none;
  }

  .headshot { height: 316px; width: 100%; }
  .headshot--outdoor {
    background: linear-gradient(180deg, var(--outdoor-sky) 0%, var(--outdoor-mid) 55%, var(--outdoor-grass) 100%);
  }
  .headshot--studio {
    background: radial-gradient(circle at 50% 40%, var(--studio-warm) 0%, var(--studio-deep) 100%);
  }

  .offer { position: relative; padding: 26px 0 0 20px; }
  .offer__row { display: flex; align-items: flex-start; }
  .offer__percent {
    font-size: 72px;
    line-height: 64px;
    font-weight: 600;
    letter-spacing: -1px;
  }
  .offer__arrow { margin: 24px 8px 0 10px; }
  .offer__price { padding-top: 4px; }
  .offer__now {
    font-size: 42px;
    line-height: 36px;
    font-weight: 600;
  }
  .offer__was {
    font-size: 12.5px;
    line-height: 14px;
    font-weight: 400;
    color: var(--ink-soft);
    margin-left: -2px;
  }
  .offer__tagline {
    margin-top: 22px;
    font-size: 20px;
    line-height: 22px;
    font-weight: 500;
  }
</style>
</head>
<body>

<article class="coupon coupon--outdoor">
  <header class="coupon__header">
    <div class="brand">
      <span class="brand__square"></span>
      <span class="brand__name">Frame Brightly</span>
    </div>
    <p class="contact">
      Text Owen Hartley on<br>07942 316 587<br>to book your session
      <a class="contact__web" href="https://www.framebrightly.co.uk">www.framebrightly.co.uk</a>
    </p>
  </header>
  <div class="headshot headshot--outdoor" role="img" aria-label="Client headshot photographed outdoors, young man in a denim jacket against a soft sky and grass background"></div>
  <section class="offer">
    <div class="offer__row">
      <span class="offer__percent">20%</span>
      <svg class="offer__arrow" width="7" height="9" viewBox="0 0 7 9" aria-hidden="true"><path d="M0 0 L7 4.5 L0 9 Z" fill="#ffffff"/></svg>
      <div class="offer__price">
        <div class="offer__now">£120</div>
        <div class="offer__was">normal price £150</div>
      </div>
    </div>
    <p class="offer__tagline">off your next headshot session</p>
  </section>
</article>

<article class="coupon coupon--studio">
  <header class="coupon__header">
    <div class="brand">
      <span class="brand__square"></span>
      <span class="brand__name">Frame Brightly</span>
    </div>
    <p class="contact">
      Text Owen Hartley on<br>07942 316 587<br>to book your session
      <a class="contact__web" href="https://www.framebrightly.co.uk">www.framebrightly.co.uk</a>
    </p>
  </header>
  <div class="headshot headshot--studio" role="img" aria-label="Client studio headshot, young man in a navy top against a warm amber backdrop"></div>
  <section class="offer">
    <div class="offer__row">
      <span class="offer__percent">20%</span>
      <svg class="offer__arrow" width="7" height="9" viewBox="0 0 7 9" aria-hidden="true"><path d="M0 0 L7 4.5 L0 9 Z" fill="#ffffff"/></svg>
      <div class="offer__price">
        <div class="offer__now">£120</div>
        <div class="offer__was">normal price £150</div>
      </div>
    </div>
    <p class="offer__tagline">off your next headshot session</p>
  </section>
</article>

</body>
</html>
```